Brantley Advisory Group provides support for renewable energy projects to utilities and suppliers

I need a professional looking business card that is both simple and elegant and unique. My clients are mostly large organizations not individuals. I am a consultant with my own company that is small but would like to give clients the impression I am larger. Smart grid, fiber optics, software, field hardware, distribution automation, substation automation, operations, energy storage/batteries, microgrids, customer service, strategy/roadmaps, conservation, Automated Metering Infrastruture (AMI or smart meters) are all areas of focus.

Target Market(s)

Utilities, suppliers, governmental agencies involved in energy. All types of energy especially natural gas and electrical. Especially renewable energy or green projects.

Contact Information for Business Card

Name - Mark Brantley Cell Phone - 425.318.2746 Email - mbrantley@brantleyag-example.com
Company - Brantley Advisory Group (logo) Title - Principal

Font styles to use
Serif
Sans Serif

Colors

Designer to choose colors to be used in the design.

Requirements
Must have
• Simple and professional and powerful.
• Unique/creative design.
Nice to have
• Utilize color scheme to accent logo colors. Maybe some geometric pattern on edge of card with color.
Should not have
• Busy, complicated, traditional

```html
<!DOCTYPE html>
<html lang="en">
<head>
<meta charset="utf-8">
<title>Brantley Advisory Group – Business Card</title>
<link rel="stylesheet" href="https://fonts.googleapis.com/css2?family=Montserrat:wght@600;700&display=swap">
<style>
  :root {
    --canvas-grey: #d1d2d4;
    --brand-blue: #1f3c96;
    --brand-blue-deep: #0a1a5c;
    --brand-navy: #020a2e;
    --brand-green: #5f8f37;
    --brand-green-deep: #2f5a1b;
    --paper: #ffffff;
    --steel: #a5a4a7;
  }
  * { margin: 0; padding: 0; box-sizing: border-box; }
  html, body {
    width: 984px; height: 1200px; overflow: hidden;
    background: var(--canvas-grey);
  }
  .canvas { position: relative; width: 984px; height: 1200px; }
  .card {
    position: absolute; left: 33px; width: 913px; height: 547px;
    overflow: hidden; background: var(--paper);
  }
  .card--front { top: 34px; }
  .card--back { top: 615px; }
  .card__art { position: absolute; inset: 0; width: 100%; height: 100%; }

  .wordmark {
    position: absolute; display: flex; align-items: center; gap: 16px;
    font-family: "Montserrat", sans-serif; font-weight: 700;
  }
  .wordmark__square { width: 58px; height: 58px; border: 4px solid currentColor; border-radius: 5px; flex: none; }
  .wordmark__name { line-height: 1.05; }
  .wordmark__primary { display: block; font-size: 44px; letter-spacing: 0.5px; }
  .wordmark__secondary { display: block; font-size: 24px; letter-spacing: 0.3px; }
  .wordmark--front { left: 50px; top: 112px; color: var(--brand-blue); }
  .wordmark--back { left: 0; right: 0; top: 212px; justify-content: center; color: var(--paper); }
  .wordmark--back .wordmark__primary { font-size: 52px; }
  .wordmark--back .wordmark__secondary { font-size: 28px; }
  .wordmark--back .wordmark__square { width: 70px; height: 70px; }

  .holder {
    position: absolute; left: 540px; top: 96px; color: var(--paper);
    font-family: "Montserrat", sans-serif; font-weight: 700; text-transform: uppercase;
  }
  .holder__name { font-size: 38px; line-height: 1; letter-spacing: 0.5px; }
  .holder__title { font-size: 25px; margin-top: 12px; font-weight: 600; }

  .contact {
    position: absolute; left: 0; color: var(--paper); text-align: right;
    font-family: "Montserrat", sans-serif; font-weight: 600; white-space: nowrap;
    line-height: 1;
  }
  .contact--phone { top: 333px; width: 594px; font-size: 36px; letter-spacing: 1px; }
  .contact--email { top: 415px; width: 636px; font-size: 24px; }
</style>
</head>
<body>
<main class="canvas">

  <section class="card card--front" aria-label="Business card front">
    <svg class="card__art" viewBox="0 0 913 547">
      <defs>
        <linearGradient id="greenField" x1="0" y1="1" x2="1" y2="0">
          <stop offset="0" stop-color="var(--brand-green-deep)"/>
          <stop offset="0.45" stop-color="var(--brand-green)"/>
          <stop offset="1" stop-color="#6c9c42"/>
        </linearGradient>
        <linearGradient id="blueField" x1="0" y1="0" x2="1" y2="1">
          <stop offset="0" stop-color="var(--brand-blue)"/>
          <stop offset="0.35" stop-color="var(--brand-blue-deep)"/>
          <stop offset="0.7" stop-color="var(--brand-blue)"/>
        </linearGradient>
        <linearGradient id="steelField" x1="0" y1="0" x2="0" y2="1">
          <stop offset="0" stop-color="#ffffff"/>
          <stop offset="1" stop-color="var(--steel)"/>
        </linearGradient>
        <linearGradient id="edgeStripe" x1="0" y1="0" x2="0" y2="1">
          <stop offset="0" stop-color="#000"/>
          <stop offset="0.5" stop-color="#555"/>
          <stop offset="1" stop-color="#fff" stop-opacity="0"/>
        </linearGradient>
        <linearGradient id="swoosh" x1="0" y1="0" x2="1" y2="0">
          <stop offset="0" stop-color="#fff" stop-opacity="0"/>
          <stop offset="0.5" stop-color="#fff" stop-opacity="0.9"/>
          <stop offset="1" stop-color="#fff"/>
        </linearGradient>
        <linearGradient id="blueEdge" x1="0" y1="0" x2="0" y2="1">
          <stop offset="0" stop-color="var(--brand-navy)"/>
          <stop offset="0.6" stop-color="#777"/>
          <stop offset="1" stop-color="#333"/>
        </linearGradient>
      </defs>

      <path d="M372,0 H397 L490,200 C480,190 470,175 462,160 Z" fill="url(#edgeStripe)"/>
      <path class="green-panel" role="img" aria-label="Green panel with faint overlapping square pattern"
            d="M397,0 H913 V258 H567 C535,258 515,248 502,225 Z" fill="url(#greenField)"/>

      <path d="M600,258 H913 V547 H753 Z" fill="url(#steelField)"/>
      <path d="M0,258 H610 C640,258 655,270 666,292 L768,547 H0 Z" fill="url(#blueEdge)"/>
      <path class="blue-panel" role="img" aria-label="Blue panel with faint overlapping square pattern"
            d="M0,258 H600 C628,258 643,270 652,290 L753,547 H0 Z" fill="url(#blueField)"/>

      <path d="M230,290 H572 C600,290 612,300 622,320 L698,500" fill="none"
            stroke="url(#swoosh)" stroke-width="5"/>

      <g class="icon icon--phone">
        <circle cx="647" cy="338" r="36" fill="var(--brand-blue)"/>
        <circle cx="642" cy="337" r="34" fill="var(--paper)"/>
        <rect x="630" y="317" width="22" height="38" rx="4" fill="none"
              stroke="var(--brand-green)" stroke-width="3" transform="rotate(-12 641 336)"/>
      </g>
      <g class="icon icon--email">
        <circle cx="688" cy="428" r="36" fill="var(--brand-blue)"/>
        <circle cx="683" cy="427" r="34" fill="var(--paper)"/>
        <g transform="rotate(-25 683 428)">
          <rect x="666" y="416" width="34" height="24" fill="var(--brand-green)"/>
          <path d="M666,416 L683,430 L700,416" fill="none" stroke="var(--paper)" stroke-width="2.5"/>
        </g>
      </g>
    </svg>

    <div class="wordmark wordmark--front">
      <span class="wordmark__square"></span>
      <span class="wordmark__name">
        <span class="wordmark__primary">BRANTLEY</span>
        <span class="wordmark__secondary">Advisory Group</span>
      </span>
    </div>

    <div class="holder">
      <p class="holder__name">Mark Brantley</p>
      <p class="holder__title">Principal</p>
    </div>

    <p class="contact contact--phone">425.318.2746</p>
    <p class="contact contact--email">mbrantley@brantleyag-example.com</p>
  </section>

  <section class="card card--back" aria-label="Business card back">
    <svg class="card__art" viewBox="0 0 913 547">
      <defs>
        <linearGradient id="backField" x1="0" y1="1" x2="1" y2="0">
          <stop offset="0" stop-color="#000000"/>
          <stop offset="0.3" stop-color="var(--brand-blue-deep)"/>
          <stop offset="0.6" stop-color="var(--brand-blue)"/>
          <stop offset="1" stop-color="var(--brand-blue)"/>
        </linearGradient>
      </defs>
      <rect class="back-panel" role="img" aria-label="Deep blue field with faint overlapping square pattern"
            width="913" height="547" fill="url(#backField)"/>
    </svg>

    <div class="wordmark wordmark--back">
      <span class="wordmark__square"></span>
      <span class="wordmark__name">
        <span class="wordmark__primary">BRANTLEY</span>
        <span class="wordmark__secondary">Advisory Group</span>
      </span>
    </div>
  </section>

</main>
</body>
</html>
```